Yellow Page Ad

We require a two full page,full colour, side by side yellow page ad.
Each page is sized 259mm[H]x210mm[W]
This would be listed under the "wholesale distributor" section of the yellow pages.

We are a wholesale distribution company.
Please see attached a past sketch of this ad we have created, however our director did not like.

The following are the departments we would like to highlight:
1.General Variety Mechandise
2.Corporate Promotional Items
3.Beverages
4.Complete Packaging Solutions(Restuarant & Fast Food Packaging)

For your reference, we have also attached our company profile.

Wholesale

```html
<!DOCTYPE html>
<html lang="en">
<head>
<meta charset="utf-8">
<title>Kestrel Supply Ltd – Wholesale</title>
<link rel="stylesheet" href="https://fonts.googleapis.com/css2?family=Paytone+One&family=Alegreya+Sans+SC:ital,wght@0,700;0,800;0,900;1,900&family=Bodoni+Moda:wght@700&family=Open+Sans:wght@400;600;700&family=Archivo+Black&display=swap">
<style>
:root{
  --red:#e8262a;
  --teal-dark:#0d7f75;
  --teal:#1aa597;
  --teal-light:#4fc7b8;
  --blue:#1740b8;
  --navy:#0b2a8c;
  --yellow:#ffe600;
  --ink:#111;
  --white:#fff;
}
*{margin:0;padding:0;box-sizing:border-box}
html,body{width:1200px;height:740px;overflow:hidden;background:var(--white)}
.ad{position:relative;width:1200px;height:740px;overflow:hidden;font-family:"Open Sans",sans-serif;color:var(--ink)}
.backdrop{position:absolute;left:0;top:0;width:1200px;height:490px;
  background:linear-gradient(180deg,#f4f8fa 0%,#e5f1f6 30%,#c9e6f5 55%,#c8b9ee 72%,#d8f2fb 88%,#eef9fd 100%)}
.brand{position:absolute;left:22px;top:12px;width:250px;height:110px}
.brand-mark{position:absolute;left:14px;top:6px;width:84px;height:84px;border-radius:50%;background:#2f5fa8}
.brand-name{position:absolute;left:108px;top:28px;font-weight:700;font-size:22px;line-height:1.05;color:var(--navy)}
.brand-tag{position:absolute;left:4px;top:94px;font-weight:700;font-size:12px;color:var(--ink)}
.headline{position:absolute;left:298px;top:24px;font-family:"Paytone One",sans-serif;font-size:61px;font-weight:400;color:var(--red);letter-spacing:1px;word-spacing:12px;line-height:1;white-space:nowrap}
.intro{position:absolute;left:294px;top:116px;width:840px;font-size:19px;line-height:1.35;color:var(--ink)}
.intro b{text-decoration:underline;font-weight:700}
.profit-art{position:absolute;left:962px;top:342px;width:200px;height:80px;border-radius:8px;
  background:linear-gradient(135deg,#c9e94a,#7ab52a 60%,#4d8f1c)}
.dept{position:absolute;top:186px;width:236px;height:160px;border-radius:50%;
  background:linear-gradient(135deg,var(--teal-light),var(--teal) 45%,var(--teal-dark));
  box-shadow:0 4px 8px rgba(0,0,0,.3);display:flex;align-items:center;justify-content:center;text-align:center;
  font-family:"Alegreya Sans SC",sans-serif;font-weight:800;color:var(--white);font-size:27px;line-height:1.2;padding:0 10px}
.dept.one{left:50px}
.dept.two{left:313px}
.dept.three{left:576px;font-size:34px}
.dept.four{left:838px;top:180px;font-size:21px;line-height:1.18;white-space:nowrap}
.dept small{display:block;font-size:15px;font-weight:700;line-height:1.3}
.burst{position:absolute;left:1035px;top:135px;width:150px;height:120px}
.slogan{position:absolute;left:180px;top:368px;width:236px;font-family:"Bodoni Moda",serif;font-weight:700;font-size:22px;line-height:1.2;text-align:right;white-space:nowrap;color:var(--ink)}
.truck{position:absolute;left:515px;top:342px;width:128px;height:98px;border-radius:6px;
  background:linear-gradient(180deg,#ffe54a,#f3c300)}
.note{position:absolute;left:668px;top:388px;font-family:"Bodoni Moda",serif;font-weight:700;font-size:21px;white-space:nowrap;color:var(--ink)}
.visit{position:absolute;left:0;width:1200px;top:444px;line-height:1;text-align:center;font-family:"Alegreya Sans SC",sans-serif;font-weight:900;font-style:italic;font-size:41px;color:var(--blue);letter-spacing:1px;white-space:nowrap;
  text-shadow:1px 1px 0 #fff}
.showroom{position:absolute;left:0;top:490px;width:1200px;height:120px;
  background:linear-gradient(180deg,#f3f4f4,#d9dcdd 60%,#eceeef)}
.hours{position:absolute;left:25px;top:593px;width:546px;height:31px;background:var(--blue);border:2px solid var(--navy);
  color:var(--yellow);font-family:"Alegreya Sans SC",sans-serif;font-weight:800;font-size:18px;line-height:27px;padding-left:14px;white-space:nowrap;word-spacing:2px}
.footer{position:absolute;left:0;top:626px;width:1200px;height:114px;background:var(--white)}
.partners{position:absolute;left:30px;top:636px;width:560px;display:flex;flex-wrap:wrap;gap:8px 9px;align-items:center}
.partner{height:24px;border-radius:4px}
.partner.round{width:36px;height:36px;border-radius:50%}
.contact{position:absolute;left:600px;top:634px;white-space:nowrap}
.web{font-weight:700;font-size:28px;line-height:1.2;color:var(--blue)}
.email,.address{font-weight:700;font-size:16px;color:#222;line-height:1.4}
.phones{position:absolute;left:980px;top:626px;font-family:"Archivo Black",sans-serif;font-size:34px;line-height:1.12;color:var(--ink)}
</style>
</head>
<body>
<div class="ad">
  <div class="backdrop" role="img" aria-label="Soft faded photograph of the company warehouse front on a bright sky"></div>

  <div class="brand">
    <div class="brand-mark"></div>
    <div class="brand-name">Kestrel<br>Supply Ltd</div>
    <div class="brand-tag">Your global sourcing experts!</div>
  </div>

  <h1 class="headline">Maximize your profits</h1>
  <p class="intro">We offer the <b>largest</b> selection of <b>high</b> quality merchandise from the best factories throughout the world guaranteeing you <b>higher</b> margins.</p>

  <div class="profit-art" role="img" aria-label="Illustration of the word Profit with a rising green arrow"></div>

  <div class="dept one">General Variety<br>Mechandise</div>
  <div class="dept two">Corporate<br>Promotional<br>Items</div>
  <div class="dept three">Beverages</div>
  <div class="dept four"><span>Complete<br>Packaging Solutions<small>(Restaurant &amp; Fast Food<br>Packaging)</small></span></div>

  <svg class="burst" viewBox="0 0 150 120" aria-label="New arrivals daily">
    <polygon fill="#e8262a" points="75,2 86,30 118,8 106,40 148,40 112,60 146,84 104,80 112,116 82,90 66,118 58,86 22,106 36,74 2,62 38,50 18,20 56,32"/>
    <text x="78" y="44" transform="rotate(24 78 60)" text-anchor="middle" font-family="Open Sans,sans-serif" font-weight="700" font-size="15" fill="#fff">New</text>
    <text x="78" y="61" transform="rotate(24 78 60)" text-anchor="middle" font-family="Open Sans,sans-serif" font-weight="700" font-size="15" fill="#fff">Arrivals</text>
    <text x="78" y="78" transform="rotate(24 78 60)" text-anchor="middle" font-family="Open Sans,sans-serif" font-weight="700" font-size="15" fill="#fff">daily!</text>
  </svg>

  <p class="slogan">From factory floor…<br>to your door…</p>
  <div class="truck" role="img" aria-label="Illustration of a yellow delivery truck with a sign reading Free Deliveries Nationwide"></div>
  <p class="note">Wholesale enquiries only</p>

  <p class="visit">Come visit our fully stocked 10,000 sq ft showroom Today!</p>

  <div class="showroom" role="img" aria-label="Panoramic photograph of the showroom interior with stocked white shelving"></div>
  <div class="hours">Mon-Fri: 8:30am-4:30pm &nbsp;Sat: 8:30am-2:30pm &nbsp;Sun: Seasonal</div>

  <div class="footer"></div>
  <div class="partners" aria-label="Partner brands">
    <span class="partner" style="width:60px;background:#c9d3e4"></span>
    <span class="partner" style="width:52px;background:#d6e7f4"></span>
    <span class="partner" style="width:52px;background:#d6e0ef"></span>
    <span class="partner" style="width:56px;background:#d4e8f4"></span>
    <span class="partner" style="width:58px;background:#d8d8d8"></span>
    <span class="partner" style="width:44px;background:#f2c2c2"></span>
    <span class="partner" style="width:54px;background:#f0d0c8"></span>
    <span class="partner" style="width:64px;background:#d9e1ec"></span>
    <span class="partner round" style="background:#e8a0a0"></span>
    <span class="partner round" style="background:#9a9a9a"></span>
    <span class="partner" style="width:58px;background:#f7d64a"></span>
    <span class="partner" style="width:50px;background:#cfcfcf"></span>
    <span class="partner" style="width:62px;background:#c8d4f0"></span>
    <span class="partner" style="width:54px;background:#f0c4c4"></span>
    <span class="partner" style="width:54px;background:#f4c6c6"></span>
    <span class="partner round" style="background:#e24a4a"></span>
    <span class="partner round" style="background:#2d7a3a"></span>
    <span class="partner round" style="background:#3a2e28"></span>
    <span class="partner round" style="background:#9ab8e0"></span>
  </div>

  <div class="contact">
    <div class="web">www.kestrelsupply.com</div>
    <div class="email">Email: sales@kestrelsupply.com</div>
    <div class="address">#7 Harbour Road, Palmview East, Marlowe.</div>
  </div>
  <div class="phones">555-4KSL<br>555-4575</div>
</div>
</body>
</html>
```